Inspirational Quote Poster for Employees

For this project, we need a simple yet high-impact poster template that will be customized for each of our employees with a personalized inspirational quote and color scheme. This template should allow us to quickly and easily customize the text and colors in the poster without a lot of effort.

The poster design should consist of:
- A stylized text area to contain the main text of the quote
- A separate text area to contain the source of quote
- A background that complements the color and style of the text

Text may use different typographic effects (such as color, stroke weight, italicization, font size changes, drop shadows) to draw attention to words in the quote; the source of the quote may be formatted the same as the main text of the quote, or may be formatted differently to distinguish it from the main quote.

The background may be simply a single color, subtle texture, gradients, halftone effects, or other color/texture effects may be used to complement the text.

Examples of the types of posters envisioned by this project:
- http://www.tackvale.com/corwinpmaddox/artquarry-job-1/

Sample quotes to use to build your poster - choose whichever one you want, but be certain that the poster design will handle both long and short quotes:
- "Happiness in intelligent people is the rarest thing I know" - Bertram Faulconer
- "Wanting to be someone else is a waste of the person you are." - Miles Tavenor
- "Experience is not what happens to you. It is what you do with what happens to you." - Cyril Pembrage
- "Simplicity is the ultimate in sophistication." - Ottaviano Restelli
- "You will get all you want in life if you help enough other people get what they want." - Hap Dunmore
- "Hell, there are no rules here — we're trying to accomplish something." - Walter Brisbane

Quote

• Final deliverable must be:
• - Formatted for an 18” x 24” poster (in portrait orientation)
• - Delivered in Adobe InDesign, Adobe Illustrator, or Extended PostScript format
• - Use CMYK color mode
• - Be print-ready at 300dpi resolution
• - Include any fonts used in the template

```html
<!DOCTYPE html>
<html lang="en">
<head>
<meta charset="utf-8">
<title>Inspirational Quote Poster</title>
<link href="https://fonts.googleapis.com/css2?family=Fredoka:wght@600;700&display=swap" rel="stylesheet">
<style>
  :root {
    --quote-orange: #e0801a;
    --quote-outline: #ffffff;
    --quote-shadow: rgba(92, 38, 110, 0.55);
    --source-purple: #7a2a96;
    --sky-white: #fffaf2;
    --glow-yellow: #ffe34a;
    --glow-gold: #f6b52a;
    --canopy-purple: #8a4a9a;
    --canopy-magenta: #c0559a;
    --warm-red: #e8505a;
  }
  * { margin: 0; padding: 0; box-sizing: border-box; }
  html, body {
    width: 848px;
    height: 1200px;
    overflow: hidden;
    background: var(--sky-white);
  }
  .poster {
    position: relative;
    width: 848px;
    height: 1200px;
    overflow: hidden;
    font-family: "Fredoka", "Varela Round", sans-serif;
  }
  .backdrop-photo {
    position: absolute;
    inset: 0;
    background:
      radial-gradient(ellipse 520px 380px at 560px 120px, rgba(138, 74, 154, 0.85), rgba(138, 74, 154, 0) 75%),
      radial-gradient(ellipse 360px 300px at 120px 80px, rgba(160, 70, 130, 0.8), rgba(160, 70, 130, 0) 75%),
      radial-gradient(ellipse 300px 420px at 110px 360px, rgba(232, 80, 90, 0.55), rgba(232, 80, 90, 0) 75%),
      radial-gradient(ellipse 220px 620px at 80px 820px, rgba(246, 181, 42, 0.95), rgba(255, 227, 74, 0) 80%),
      radial-gradient(ellipse 700px 200px at 424px 1190px, rgba(255, 210, 60, 0.9), rgba(255, 227, 74, 0) 80%),
      radial-gradient(ellipse 220px 260px at 560px 820px, rgba(240, 140, 60, 0.45), rgba(240, 140, 60, 0) 80%),
      var(--sky-white);
  }
  .quote {
    position: absolute;
    left: 103px;
    top: 112px;
    font-weight: 700;
    font-size: 86px;
    line-height: 105px;
    letter-spacing: 1px;
    color: var(--quote-orange);
    -webkit-text-stroke: 9px var(--quote-outline);
    paint-order: stroke fill;
    text-shadow: 8px 10px 10px var(--quote-shadow);
  }
  .quote-line { display: block; white-space: nowrap; }
  .quote-source {
    position: absolute;
    left: 146px;
    top: 718px;
    font-weight: 600;
    font-size: 30px;
    color: var(--source-purple);
    -webkit-text-stroke: 6px var(--quote-outline);
    paint-order: stroke fill;
    text-shadow: 3px 4px 5px rgba(92, 38, 110, 0.35);
    white-space: nowrap;
  }
</style>
</head>
<body>
  <main class="poster">
    <div class="backdrop-photo" role="img" aria-label="Sunlit photograph of a large tree with a girl swinging on a rope swing, washed in purple, red and yellow light"></div>
    <blockquote class="quote">
      <span class="quote-line">”Happiness</span>
      <span class="quote-line">in Intelligent</span>
      <span class="quote-line">people is</span>
      <span class="quote-line">the rarest</span>
      <span class="quote-line">thing I know”</span>
    </blockquote>
    <p class="quote-source">- Bertram Faulconer</p>
  </main>
</body>
</html>
```